Business Card Design Project

I am community manager and social media strategist. I need a double sided business card with company logo and name. Looking for something professional, elegant but also a little bit original.

• - The logo and the colours are the company colours and a required to stay.
- The size should be: 84 x 55 mm (or 3.30 x 2.16)
- The file size should be: 1039 x 697 pixels (300 dpi)
- I'd like rounded corners. :)

Use the following contact information for the card:

Léonie Vardin
Stratégie médias sociaux / community management / édition de sites sociaux
mob. : 0687529103
leonie.vardin@postelune.fr
Twitter. : @lvardin
Skype : vardin.leonie

```html
<!DOCTYPE html>
<html lang="fr">
<head>
<meta charset="utf-8">
<title>Léonie Vardin – Carte de visite</title>
<link rel="stylesheet" href="https://fonts.googleapis.com/css2?family=Barlow:wght@400;500;600&display=swap">
<style>
  :root {
    --page: #ffffff;
    --card-deep: #0d5a92;
    --card-mid: #136ea8;
    --card-light: #1682bd;
    --ink: #ffffff;
    --ink-soft: #e3eef7;
    --rule: #0a3f68;
    --shadow: rgba(0, 0, 0, 0.45);
  }
  * { margin: 0; padding: 0; box-sizing: border-box; }
  html, body {
    width: 1200px;
    height: 900px;
    overflow: hidden;
    background: var(--page);
    font-family: "Barlow", Arial, sans-serif;
    color: var(--ink);
  }
  .canvas { position: relative; width: 1200px; height: 900px; }

  .card {
    position: absolute;
    width: 505px;
    height: 330px;
    border-radius: 42px;
    overflow: hidden;
    background: linear-gradient(200deg, var(--card-light) 0%, var(--card-mid) 45%, var(--card-deep) 100%);
    box-shadow: 10px 12px 14px var(--shadow);
  }
  .card--front { left: 60px; top: 283px; }
  .card--back { left: 637px; top: 285px; }

  .card__wash {
    position: absolute;
    inset: 0;
  }
  .card--front .card__wash {
    background: radial-gradient(ellipse 70% 90% at 20% 40%, rgba(255,255,255,0.14), rgba(255,255,255,0) 70%);
  }
  .card--back .card__wash {
    background: radial-gradient(ellipse 55% 80% at 90% 25%, rgba(255,255,255,0.14), rgba(255,255,255,0) 70%);
  }

  .brand {
    position: absolute;
    left: 285px;
    top: 100px;
    width: 140px;
    display: flex;
    flex-direction: column;
    align-items: center;
  }
  .brand__dot {
    width: 78px;
    height: 78px;
    border-radius: 50%;
    background: var(--ink);
    margin-bottom: 16px;
  }
  .brand__name {
    font-size: 34px;
    font-weight: 600;
    letter-spacing: 2px;
    line-height: 1;
    color: var(--ink);
  }

  .identity {
    position: absolute;
    right: 259px;
    top: 112px;
    text-align: right;
  }
  .identity__name {
    font-size: 36px;
    font-weight: 500;
    letter-spacing: 0.5px;
    line-height: 40px;
    margin-bottom: 2px;
  }
  .identity__role {
    font-size: 18px;
    font-weight: 400;
    line-height: 23px;
    color: var(--ink-soft);
  }

  .divider {
    position: absolute;
    left: 265px;
    top: 108px;
    width: 2px;
    height: 116px;
    background: var(--rule);
  }

  .contact {
    position: absolute;
    left: 281px;
    top: 122px;
    list-style: none;
  }
  .contact li {
    font-size: 18px;
    line-height: 25.5px;
    color: var(--ink-soft);
    letter-spacing: 0.3px;
  }
</style>
</head>
<body>
  <main class="canvas">
    <section class="card card--front" aria-label="Recto">
      <div class="card__wash"></div>
      <div class="brand">
        <div class="brand__dot"></div>
        <div class="brand__name">VENTORIA</div>
      </div>
    </section>

    <section class="card card--back" aria-label="Verso">
      <div class="card__wash"></div>
      <div class="identity">
        <h1 class="identity__name">Léonie Vardin</h1>
        <p class="identity__role">Stratégie médias sociaux</p>
        <p class="identity__role">Community management</p>
        <p class="identity__role">Édition de sites sociaux</p>
      </div>
      <div class="divider"></div>
      <ul class="contact">
        <li>mob. 0687529103</li>
        <li>leonie.vardin@postelune.fr</li>
        <li>Twitter @lvardin</li>
        <li>Skype vardin.leonie</li>
      </ul>
    </section>
  </main>
</body>
</html>
```